Wine Label Logo NEW name too

We would like to see this done in more colors but, lighter ones too. the dark colors don't show up that well. Can you also do some on white wine and not just red wine?

Also, we aren't sure we will use the name Plumvelle and wonder if you could use the name Nutmeadow with the same design to see how that looks, as well?

new wine label for a brand called Plumvelle (one word) and is targeted to go after 21-40 year olds. Probably more women than men. There will be Plumvelle Red, Plumvelle White, Plumvelle Cabernet, etc. the profile of the wine will be sweet...duh!!

would love you to come up with some TAG LINE ideas, as well. Size should be between 2 1/2 to 3 inches wide and 5 to 6 inches long. Needs place holders for varietal, Cabernet. 13.5% alcohol, area wil be California. I suggest you look at a bunch of wine labels to better understand this brief.

The final design should communicate fun, sweet, wine, young, hip

Wine labels matter. Period. Now, attempting to define “fun and contemporary” is nigh on impossible, but I think it would be safe to assume that this could mean “non-traditional.” Let’s face it. Design matters to millennial consumers. Quill, Tern Lodges, Hearthline Magazine – these brands are not ONLY for millennials by any means (well, maybe Tern), but design is top priority for these brands, and these brands have top priority for millennials. Feel free to do the math. If we spend money on something, we expect it to be beautiful and often times we expect social purchases like wine to act as a public reflection of our tastes and personality. This latter expectation is no different than any other generation (if arguably more intense due to our intrinsic personal branding tendencies); however, our personalities and what we are reflecting out to our peers IS different.
Updates

What about a label that is 2 1/2 to 3 inches wide and 5-6 inches long and looks like a white or off white piece of paper that has had berries poured across it with some stains and the name Plumvelle Cabernet as the logo on the label?  Needs space for the AVA area grown to say California and the vintage 2011 and alcohol level in small letters 12.3%. 

Look at some wine labels to get a unique idea. Needs to appeal to 21-40 year old women. Needs to denote the wine is sweet

Reason: two partners are out of the country and I want them involved in the choice

Target Market(s)

Industry/Entity Type

Social

Logo Text

Plumvelle Cabernet

Logo styles of interest
Pictorial/Combination Logo
Abstract Logo
Wordmark Logo

```html
<!DOCTYPE html>
<html lang="en">
<head>
<meta charset="utf-8">
<title>Plumvelle Wine Labels</title>
<link rel="stylesheet" href="https://fonts.googleapis.com/css2?family=Playfair+Display:wght@700&family=Crimson+Text:wght@400;600&display=swap">
<style>
  :root {
    --page: #f1efec;
    --label-w: 210px;
    --label-h: 262px;
  }
  * { box-sizing: border-box; margin: 0; padding: 0; }
  html, body { width: 1200px; height: 900px; overflow: hidden; }
  body {
    background: var(--page);
    display: flex;
    align-items: center;
    justify-content: center;
    gap: 25px;
    font-family: "Crimson Text", Georgia, serif;
  }

  .label--cabernet {
    --label-base: #b0227a; --label-deep: #6e2a86;
    --art-light: #d03a8e; --art-dark: #3a1830;
    --wordmark: #ffffff; --ink: #ffffff;
  }
  .label--sauvignon-blanc {
    --label-base: #e6e8de; --label-deep: #c9ccc0;
    --art-light: #f3f4ef; --art-dark: #a4a69c;
    --wordmark: #ffffff; --ink: #55564f;
  }
  .label--cabernet-sauvignon {
    --label-base: #c41e4a; --label-deep: #8e1438;
    --art-light: #e0306a; --art-dark: #3a1220;
    --wordmark: #ffffff; --ink: #ffffff;
  }
  .label--chardonnay {
    --label-base: #ede7c6; --label-deep: #d4cba0;
    --art-light: #f4f0d8; --art-dark: #b0a47e;
    --wordmark: #ffffff; --ink: #675f45;
  }
  .label--merlot {
    --label-base: #d8222e; --label-deep: #a8141e;
    --art-light: #ee4048; --art-dark: #3a1014;
    --wordmark: #ffffff; --ink: #ffffff;
  }

  .label {
    position: relative;
    width: var(--label-w);
    height: var(--label-h);
    background: linear-gradient(100deg, var(--label-base) 0%, var(--label-base) 55%, var(--label-deep) 100%);
    overflow: hidden;
  }
  .label__art {
    position: absolute;
    left: 0;
    right: 0;
    top: 96px;
    bottom: 0;
    background: linear-gradient(100deg, var(--art-dark) 0%, var(--art-light) 45%, var(--label-deep) 100%);
  }
  .label__text {
    position: absolute;
    left: 22px;
    top: 18px;
    color: var(--ink);
  }
  .label__wordmark {
    font-family: "Playfair Display", Georgia, serif;
    font-weight: 700;
    font-size: 27px;
    letter-spacing: -0.5px;
    line-height: 1;
    color: var(--wordmark);
  }
  .label__varietal {
    margin-top: 10px;
    font-size: 12px;
    letter-spacing: 2px;
    line-height: 1.05;
    text-transform: uppercase;
  }
  .label__vintage-row {
    display: flex;
    align-items: flex-start;
    gap: 3px;
    margin-top: -1px;
  }
  .label__vintage {
    font-size: 27px;
    line-height: 0.95;
  }
  .label__region {
    font-size: 7px;
    letter-spacing: 2.4px;
    text-transform: uppercase;
    margin-top: 2px;
  }
  .label__abv {
    position: absolute;
    right: 38px;
    bottom: 16px;
    color: var(--ink);
    line-height: 1;
  }
  .label__abv-value { font-size: 13px; display: block; }
  .label__abv-unit { font-size: 7px; letter-spacing: 0.6px; display: block; margin-top: 1px; }
</style>
</head>
<body>

<article class="label label--cabernet">
  <div class="label__art" role="img" aria-label="Abstract arc and vertical stripe artwork in magenta and violet"></div>
  <div class="label__text">
    <h1 class="label__wordmark">Plumvelle</h1>
    <p class="label__varietal">Cabernet</p>
    <div class="label__vintage-row"><span class="label__vintage">2011</span><span class="label__region">California</span></div>
  </div>
  <p class="label__abv"><span class="label__abv-value">12.3%</span><span class="label__abv-unit">ALC/VOL</span></p>
</article>

<article class="label label--sauvignon-blanc">
  <div class="label__art" role="img" aria-label="Abstract arc and vertical stripe artwork in pale grey"></div>
  <div class="label__text">
    <h1 class="label__wordmark">Plumvelle</h1>
    <p class="label__varietal">Sauvignon<br>Blanc</p>
    <div class="label__vintage-row"><span class="label__vintage">2011</span><span class="label__region">California</span></div>
  </div>
  <p class="label__abv"><span class="label__abv-value">12.3%</span><span class="label__abv-unit">ALC/VOL</span></p>
</article>

<article class="label label--cabernet-sauvignon">
  <div class="label__art" role="img" aria-label="Abstract arc and vertical stripe artwork in crimson"></div>
  <div class="label__text">
    <h1 class="label__wordmark">Plumvelle</h1>
    <p class="label__varietal">Cabernet<br>Sauvignon</p>
    <div class="label__vintage-row"><span class="label__vintage">2011</span><span class="label__region">California</span></div>
  </div>
  <p class="label__abv"><span class="label__abv-value">12.3%</span><span class="label__abv-unit">ALC/VOL</span></p>
</article>

<article class="label label--chardonnay">
  <div class="label__art" role="img" aria-label="Abstract arc and vertical stripe artwork in cream and khaki"></div>
  <div class="label__text">
    <h1 class="label__wordmark">Plumvelle</h1>
    <p class="label__varietal">Chardonnay</p>
    <div class="label__vintage-row"><span class="label__vintage">2011</span><span class="label__region">California</span></div>
  </div>
  <p class="label__abv"><span class="label__abv-value">12.3%</span><span class="label__abv-unit">ALC/VOL</span></p>
</article>

<article class="label label--merlot">
  <div class="label__art" role="img" aria-label="Abstract arc and vertical stripe artwork in bright red"></div>
  <div class="label__text">
    <h1 class="label__wordmark">Plumvelle</h1>
    <p class="label__varietal">Merlot</p>
    <div class="label__vintage-row"><span class="label__vintage">2011</span><span class="label__region">California</span></div>
  </div>
  <p class="label__abv"><span class="label__abv-value">12.3%</span><span class="label__abv-unit">ALC/VOL</span></p>
</article>

</body>
</html>
```